Tarvel Ridge LLC

Need Professional Business cards for New Investment Fund

Target Market(s)

High Quality investors

Industry/Entity Type

Financial

Contact Information for Business Card

Phone Number +1 555 284 6193
Name Pavel Orlinsky
Title Fund Manager
email po@FundTarvel.example
Website www.FundTarvel.example

Colors

Designer to choose colors to be used in the design.

Requirements
Must have
• Must have our Logo and all of the above. Must be made so lettering and loge can be raised

```html
<!DOCTYPE html>
<html lang="en">
<head>
<meta charset="utf-8">
<title>Tarvel Ridge LLC – Business Card</title>
<link href="https://fonts.googleapis.com/css2?family=Lato:wght@400;700&display=swap" rel="stylesheet">
<style>
  :root {
    --brand-green: #5bbb47;
    --brand-dark: #3f4a42;
    --card-white: #ffffff;
    --page-bg: #e9e7e3;
    --ink-light: #ffffff;
  }
  html, body {
    margin: 0;
    padding: 0;
    width: 1200px;
    height: 1023px;
    overflow: hidden;
    background: var(--page-bg);
    font-family: "Lato", sans-serif;
  }
  .canvas {
    position: relative;
    width: 1200px;
    height: 1023px;
  }
  .card {
    position: absolute;
    left: 247px;
    width: 682px;
    height: 390px;
    overflow: hidden;
    box-shadow: -8px 8px 0 var(--brand-green), -8px 10px 0 var(--brand-dark), 2px 6px 10px rgba(0,0,0,0.25);
  }
  .card-front { top: 87px; background: var(--brand-green); }
  .card-back { top: 541px; background: var(--brand-green); }

  .front-shape { position: absolute; inset: 0; }

  .holder-name {
    position: absolute;
    left: 37px;
    top: 112px;
    margin: 0;
    font-size: 31px;
    font-weight: 700;
    color: var(--ink-light);
    letter-spacing: -0.2px;
  }
  .holder-title {
    position: absolute;
    left: 37px;
    top: 153px;
    margin: 0;
    font-size: 17px;
    font-weight: 400;
    color: var(--ink-light);
  }
  .contact-list {
    position: absolute;
    left: 37px;
    top: 192px;
    margin: 0;
    padding: 0;
    list-style: none;
  }
  .contact-item {
    display: flex;
    align-items: center;
    height: 30px;
    font-size: 18px;
    color: var(--ink-light);
  }
  .contact-icon {
    width: 16px;
    height: 16px;
    margin-right: 12px;
    flex: none;
  }

  .brand-mark {
    position: absolute;
    display: flex;
    align-items: center;
    gap: 10px;
    color: var(--brand-dark);
    font-weight: 700;
    font-size: 26px;
    letter-spacing: 1px;
    white-space: nowrap;
  }
  .brand-mark-front { left: 420px; top: 178px; }
  .brand-mark-back { left: 50%; top: 50%; transform: translate(-50%, -50%); font-size: 30px; }
  .brand-square {
    width: 18px;
    height: 18px;
    background: var(--brand-green);
    flex: none;
  }
  .brand-mark-back .brand-square { background: var(--brand-dark); }
</style>
</head>
<body>
<div class="canvas">

  <section class="card card-front" aria-label="Business card front">
    <svg class="front-shape" width="682" height="390" viewBox="0 0 682 390" aria-hidden="true">
      <path d="M386 0 C330 70 305 190 368 390 L682 390 L682 0 Z" fill="var(--brand-dark)" transform="translate(-10 0)"/>
      <path d="M386 0 C340 70 318 190 382 390 L682 390 L682 0 Z" fill="var(--card-white)"/>
    </svg>

    <h1 class="holder-name">Pavel Orlinsky</h1>
    <p class="holder-title">Fund Manager</p>

    <ul class="contact-list">
      <li class="contact-item">
        <svg class="contact-icon" viewBox="0 0 16 16" aria-hidden="true">
          <path d="M4 1.5 L6 4.5 L4.6 6 C5.4 8 7.8 10.5 10 11.4 L11.5 10 L14.5 12 L13.2 14.3 C8 14.6 1.5 8 1.7 2.8 Z" fill="var(--ink-light)"/>
          <path d="M9.5 2.5 A4.5 4.5 0 0 1 13.5 6.5 M9.3 4.6 A2.4 2.4 0 0 1 11.4 6.7" stroke="var(--ink-light)" stroke-width="1.2" fill="none"/>
        </svg>
        +1 555 284 6193
      </li>
      <li class="contact-item">
        <svg class="contact-icon" viewBox="0 0 16 16" aria-hidden="true">
          <rect x="1" y="3.5" width="14" height="9.5" fill="var(--ink-light)"/>
          <path d="M1 3.5 L8 9 L15 3.5 M1 13 L6 8 M15 13 L10 8" stroke="var(--brand-green)" stroke-width="1.1" fill="none"/>
        </svg>
        po@FundTarvel.example
      </li>
      <li class="contact-item">
        <svg class="contact-icon" viewBox="0 0 16 16" aria-hidden="true">
          <circle cx="8" cy="8" r="6.5" stroke="var(--ink-light)" stroke-width="1.2" fill="none"/>
          <ellipse cx="8" cy="8" rx="2.8" ry="6.5" stroke="var(--ink-light)" stroke-width="1" fill="none"/>
          <path d="M1.5 8 H14.5 M2.5 5 H13.5 M2.5 11 H13.5" stroke="var(--ink-light)" stroke-width="1" fill="none"/>
        </svg>
        www.FundTarvel.example
      </li>
    </ul>

    <div class="brand-mark brand-mark-front">
      <span class="brand-square"></span>
      <span class="brand-name">TARVEL RIDGE</span>
    </div>
  </section>

  <section class="card card-back" aria-label="Business card back">
    <div class="brand-mark brand-mark-back">
      <span class="brand-square"></span>
      <span class="brand-name">TARVEL RIDGE</span>
    </div>
  </section>

</div>
</body>
</html>
```